Wed site for biomedical device startup

We need a generic website for a medical device startup. I will provide examples below of websites from other companies that can serve as models for what we are looking for. The startup is for a device that can non invasively measure blood flow in the brain using light. The application is to detect the type of stroke someone is having before they get to the hospital so treatment can be started right away. This saves patients upto hours of delayed treatment. Patients will be able to recover from stroke much better and faster as a result. I have attached an AI generated illustration of what the device will ultimately look like for reference.

https://www.brightvalemedical.com
https://quintavex.com

Target Market(s)

Biomedical, medical device, investors of biomedical device startups

Industry/Entity Type

Biomedical

Coding

Coded - Design and coding required

Number of Pages Required

4 page

Requirements
Must have
• same section and section headings as example websites listed above
Nice to have
• similar to example websites listed above. Prefer a darker website over a lighter one. Perhaps dark blues to go with logo colors. A moving background image element at top of landing page could be cool. Something indicative of heartbeat, or neurons, or blood flow.

```html
<!DOCTYPE html>
<html lang="en">
<head>
<meta charset="utf-8">
<title>Lumaro — Advanced Medical Devices</title>
<link href="https://fonts.googleapis.com/css2?family=Inter+Tight:wght@400;500;600&display=swap" rel="stylesheet">
<style>
:root{
  --navy:#0b0a4a;
  --navy-line:#1c1b5e;
  --cyan:#00e0e8;
  --ink:#0b0a4a;
  --text:#1d1d2b;
  --muted:#6b6b78;
  --soft:#f7f7f8;
  --line:#e6e6ea;
  --white:#ffffff;
}
*{box-sizing:border-box;margin:0;padding:0}
html,body{width:1200px;height:4103px;overflow:hidden}
body{font-family:"Inter Tight",Arial,sans-serif;color:var(--text);background:var(--white);position:relative}
.grid-lines{position:absolute;inset:0;pointer-events:none;z-index:5}
.grid-lines span{position:absolute;top:0;bottom:0;width:0;border-left:1px dashed rgba(120,120,160,.18)}
section,header,footer{position:absolute;left:0;width:1200px}
.btn{position:absolute;display:flex;align-items:center;justify-content:center;gap:8px;border-radius:22px;font-size:13px;font-weight:500;height:42px}
.btn-cyan{background:var(--cyan);color:var(--ink)}
.btn-navy{background:var(--navy);color:var(--white)}
.btn-white{background:var(--white);color:var(--ink)}
.label{position:absolute;font-size:14px;color:var(--muted)}
.h2{position:absolute;font-weight:500;color:var(--ink);letter-spacing:-.02em;line-height:1.2}
.center{left:0;width:1200px;text-align:center}
.photo{position:absolute}
.brand{position:absolute;display:flex;align-items:center;gap:10px;font-weight:500;letter-spacing:.12em}
.brand i{display:block;border-radius:50%;background:var(--cyan)}

/* header */
.site-header{top:0;height:72px;background:var(--navy);border-bottom:1px solid var(--navy-line)}
.site-header .brand{left:66px;top:22px;color:var(--white);font-size:24px}
.site-header .brand i{width:28px;height:28px}
.nav{position:absolute;left:236px;top:29px;display:flex;gap:42px;font-size:12px;color:var(--white)}
.nav-demo{left:926px;top:20px;width:113px;height:34px;border:1px solid var(--white);color:var(--white);font-size:12px}
.nav-contact{left:1049px;top:20px;width:84px;height:34px;font-size:12px}

/* hero */
.hero{top:72px;height:589px;background:var(--navy);color:var(--white)}
.hero h1{position:absolute;left:116px;top:138px;font-size:50px;font-weight:500;line-height:1.2;letter-spacing:-.02em;width:520px}
.hero p{position:absolute;left:116px;top:336px;width:440px;font-size:14px;line-height:1.6}
.hero .btn{left:116px;top:433px;width:134px}
.hero-visual{left:700px;top:120px;width:380px;height:380px;border-radius:50%;background:radial-gradient(circle,rgba(11,10,74,1) 18%,rgba(120,120,190,.35) 45%,rgba(11,10,74,0) 70%)}

/* mission */
.mission{top:661px;height:524px}
.mission .label{left:116px;top:123px}
.mission .h2{left:116px;top:156px;font-size:42px}
.mission p{position:absolute;left:116px;top:221px;width:360px;font-size:14px;line-height:1.6;color:var(--muted)}
.mission .btn{left:116px;top:344px;width:134px}
.mission .photo{left:617px;top:79px;width:466px;height:352px;background:linear-gradient(135deg,#1f3a8a,#2c4fa8 50%,#1a2c6b)}

/* technology */
.tech{top:1185px;height:631px;background:var(--soft)}
.tech .label{top:64px}
.tech .h2{top:94px;font-size:40px}
.tech-card{position:absolute;top:198px;width:305px;text-align:center}
.tech-card .frame{background:var(--white);border:1px solid var(--line);padding:9px;height:208px}
.tech-card .photo{position:static;height:190px}
.tech-card h3{margin-top:28px;font-size:26px;font-weight:500;color:var(--ink);letter-spacing:-.02em}
.tech-card p{margin-top:10px;font-size:14px;line-height:1.6;color:var(--muted);padding:0 4px}

/* precision band */
.precision{top:1816px;height:507px;background:linear-gradient(90deg,#c9d0cf 0%,#8f9a98 35%,#3e4a4a 75%,#1f2929 100%)}
.precision .photo{left:0;top:0;width:1200px;height:507px}
.precision h2{position:absolute;left:651px;top:100px;width:460px;font-size:44px;font-weight:500;line-height:1.18;color:var(--white);letter-spacing:-.02em}
.precision p{position:absolute;left:651px;top:266px;width:420px;font-size:14px;line-height:1.6;color:var(--white)}
.precision .btn{left:651px;top:361px;width:134px}

/* solutions */
.solutions{top:2323px;height:620px}
.solutions .label{top:90px}
.solutions .h2{top:122px;font-size:40px}
.sol-card{position:absolute;top:268px;width:309px;height:290px;border:1px solid var(--line);padding:0 26px}
.sol-card svg{position:absolute;left:26px;top:56px}
.sol-card h3{position:absolute;left:26px;top:128px;font-size:26px;font-weight:500;color:var(--ink);letter-spacing:-.02em}
.sol-card p{position:absolute;left:26px;top:192px;width:250px;font-size:14px;line-height:1.6;color:var(--muted)}

/* partners */
.partners{top:2943px;height:361px}
.partners .label{top:52px}
.partners .h2{top:88px;font-size:40px}
.partner-row{position:absolute;top:200px;left:150px;width:920px;display:flex;justify-content:space-between;align-items:center}
.partner{display:flex;align-items:center;gap:8px;font-size:18px;color:#2a3a7a}
.partner i{display:block;width:24px;height:24px;background:#2a3a7a}

/* cta */
.cta{top:3304px;left:66px;width:1067px;height:384px;background:var(--navy);color:var(--white);text-align:center}
.cta h2{position:absolute;left:0;width:100%;top:80px;font-size:56px;font-weight:500;line-height:1.2;letter-spacing:-.02em}
.cta p{position:absolute;left:0;width:100%;top:224px;font-size:14px}
.cta .btn-cyan{left:386px;top:274px;width:142px}
.cta .btn-white{left:540px;top:274px;width:142px}

/* footer */
.site-footer{top:3740px;height:363px}
.site-footer .brand{left:116px;top:38px;color:var(--ink);font-size:24px}
.site-footer .brand i{width:32px;height:32px}
.foot-col{position:absolute;top:38px;font-size:13px;color:var(--text)}
.foot-col h4{font-size:13px;font-weight:400;color:var(--muted);margin-bottom:14px}
.foot-col li{list-style:none;height:30px}
.copyright{position:absolute;left:116px;top:301px;font-size:12px;color:var(--muted)}
.social{position:absolute;left:1000px;top:300px;display:flex;gap:16px}
.social i{display:block;width:17px;height:17px;border-radius:50%;background:#3a3a4a}
</style>
</head>
<body>
<div class="grid-lines" aria-hidden="true">
  <span style="left:100px"></span><span style="left:351px"></span><span style="left:601px"></span><span style="left:851px"></span><span style="left:1100px"></span>
</div>

<header class="site-header">
  <div class="brand"><i></i>LUMARO</div>
  <nav class="nav"><span>Home</span><span>About</span><span>Products</span><span>Technology</span><span>Blog</span></nav>
  <a class="btn nav-demo">Request a Demo</a>
  <a class="btn btn-cyan nav-contact">Contact us</a>
</header>

<section class="hero">
  <h1>Innovating Healthcare Through Advanced Medical Devices</h1>
  <p>Our mission is to develop cutting-edge medical technologies that enhance patient outcomes and support healthcare professionals worldwide.</p>
  <a class="btn btn-cyan">Learn More
    <svg width="12" height="12" viewBox="0 0 12 12"><path d="M1 6h9M6 2l4 4-4 4" fill="none" stroke="currentColor" stroke-width="1.5"/></svg></a>
  <div class="photo hero-visual" role="img" aria-label="Swirling dotted spiral suggesting blood flow"></div>
</section>

<section class="mission">
  <div class="label">About Us</div>
  <h2 class="h2">Our Mission</h2>
  <p>We are dedicated to addressing critical healthcare challenges by creating innovative, non-invasive medical devices that provide real-time monitoring and diagnostics.</p>
  <a class="btn btn-cyan">Learn More
    <svg width="12" height="12" viewBox="0 0 12 12"><path d="M1 6h9M6 2l4 4-4 4" fill="none" stroke="currentColor" stroke-width="1.5"/></svg></a>
  <div class="photo" role="img" aria-label="Clinicians in blue scrubs reviewing data on a tablet"></div>
</section>

<section class="tech">
  <div class="label center">Technology</div>
  <h2 class="h2 center">Innovative Solutions for Better Health</h2>
  <div class="tech-card" style="left:116px">
    <div class="frame"><div class="photo" role="img" aria-label="Researcher working at monitoring screens" style="background:linear-gradient(135deg,#1b2f5a,#3f6fa8)"></div></div>
    <h3>Non-Invasive Monitoring</h3>
    <p>Utilizing advanced optical technologies to monitor vital physiological parameters without discomfort to patients.</p>
  </div>
  <div class="tech-card" style="left:447px">
    <div class="frame"><div class="photo" role="img" aria-label="Glowing data network visual" style="background:linear-gradient(135deg,#0d1230,#3a2a5a 50%,#1a3a6a)"></div></div>
    <h3>Real-Time Data</h3>
    <p>Providing continuous, real-time data to assist clinicians in making informed decisions promptly.</p>
  </div>
  <div class="tech-card" style="left:778px">
    <div class="frame"><div class="photo" role="img" aria-label="Clinician using a laptop in a hospital" style="background:linear-gradient(135deg,#c7ccd2,#5a7398 55%,#9aa5b0)"></div></div>
    <h3>User-Centric Design</h3>
    <p>Designing devices that are intuitive and easy to integrate into existing healthcare workflows.</p>
  </div>
</section>

<section class="precision">
  <div class="photo" role="img" aria-label="Scientist in safety glasses working in a laboratory"></div>
  <h2>Precision Biomedical Devices for Enhanced Patient Outcomes</h2>
  <p>We engineer cutting-edge medical devices that combine clinical expertise with advanced technology to drive accurate diagnoses, personalized treatments, and proactive care.</p>
  <a class="btn btn-navy">Learn More
    <svg width="12" height="12" viewBox="0 0 12 12"><path d="M1 6h9M6 2l4 4-4 4" fill="none" stroke="currentColor" stroke-width="1.5"/></svg></a>
</section>

<section class="solutions">
  <div class="label center">Solutions for Healthcare Providers</div>
  <h2 class="h2 center">Tailored Tools for Modern<br>Medical Challenges</h2>
  <div class="sol-card" style="left:116px">
    <svg width="44" height="44" viewBox="0 0 44 44" fill="none" stroke="#0b0a4a" stroke-width="1.6"><rect x="4" y="14" width="36" height="26"/><path d="M4 20h36M14 4h16v10H14zM22 6v6M19 9h6M10 26h6v14h-6zM28 26h6v6h-6z"/></svg>
    <h3>For Hospitals</h3>
    <p>Streamline workflows with interoperable, hospital-grade devices.</p>
  </div>
  <div class="sol-card" style="left:446px">
    <svg width="44" height="44" viewBox="0 0 44 44" fill="none" stroke="#0b0a4a" stroke-width="1.6"><rect x="4" y="14" width="36" height="26"/><path d="M4 20h36M14 4h16v10H14zM22 6v6M19 9h6M10 26h6v14h-6zM28 26h6v6h-6z"/></svg>
    <h3>For Clinics</h3>
    <p>Cost-effective solutions for outpatient care.</p>
  </div>
  <div class="sol-card" style="left:774px">
    <svg width="44" height="44" viewBox="0 0 44 44" fill="none" stroke="#0b0a4a" stroke-width="1.6"><circle cx="22" cy="12" r="8"/><path d="M6 40v-6a10 10 0 0 1 10-10h12a10 10 0 0 1 10 10v6M16 24v8M28 24v6"/><circle cx="16" cy="34" r="2.5"/></svg>
    <h3>For Specialists</h3>
    <p>Specialized tools for cardiology, neurology, [etc.].</p>
  </div>
</section>

<section class="partners">
  <div class="label center">Partners and Collaborators</div>
  <h2 class="h2 center">Partnering with Global Research Leaders</h2>
  <div class="partner-row">
    <div class="partner"><i></i>Harlow Institute</div>
    <div class="partner"><i></i>Westbrook Clinical Research</div>
    <div class="partner"><i></i>Ridgeline Health</div>
    <div class="partner"><i></i>Ashford Innovations</div>
  </div>
</section>

<section class="cta">
  <h2>Lead the Next Wave of<br>Medical Innovation</h2>
  <p>Partner with Lumaro to integrate precision-driven devices into your practice or institution.</p>
  <a class="btn btn-cyan">Get Started Now</a>
  <a class="btn btn-white">Contact Sales</a>
</section>

<footer class="site-footer">
  <div class="brand"><i></i>LUMARO</div>
  <div class="foot-col" style="left:474px"><h4>Products</h4><ul><li>Diagnostic Devices</li><li>Therapeutic Devices</li><li>Monitoring Systems</li><li>Specifications</li><li>Request a Quote</li><li>Pricing</li></ul></div>
  <div class="foot-col" style="left:648px"><h4>Solutions</h4><ul><li>For Hospitals</li><li>For Clinics</li><li>For Specialists</li><li>Case Studies</li><li>Marketplaces</li></ul></div>
  <div class="foot-col" style="left:822px"><h4>Resources</h4><ul><li>Tutorials</li><li>Blog</li><li>Community</li><li>Privacy Policy</li></ul></div>
  <div class="foot-col" style="left:960px"><h4>About</h4><ul><li>Company</li><li>Careers</li><li>FAQ</li><li>Contact Us</li></ul></div>
  <div class="copyright">© 2025 Lumaro. All right reserved</div>
  <div class="social"><i></i><i></i><i></i></div>
</footer>
</body>
</html>
```